Edgy rebranded biz cards KRB

We are rebranding our 20 yr old mortgage company with a new logo and would like cards to compliment our new look.

Target Market(s)

potential home buyers or clients for refinance

Industry/Entity Type

Mortgage Brokerage

Contact Information for Business Card

418 W. Lomita Ave #305
Henderson, NV 89152
702.519.4827 o
702-519-4829 f
www.kestrelridgelending,example
nmls 842019
KRB is an equal housing lender

Font styles to use
Sans Serif

Colors
0455a3
3176b5
0393ce
33a6d7

Requirements
Must have
• space for a photo
Nice to have
• One side with the company info and the other with the person's info

```html
<!DOCTYPE html>
<html lang="en">
<head>
<meta charset="utf-8">
<title>Kestrel Ridge Lending – Business Cards</title>
<link href="https://fonts.googleapis.com/css2?family=Roboto:wght@400;500;700&display=swap" rel="stylesheet">
<style>
  :root {
    --blue-deep: #0455a3;
    --blue-mid: #3176b5;
    --blue-bright: #0393ce;
    --blue-soft: #33a6d7;
    --card-white: #ececec;
    --stage: #e4e6ea;
    --photo-dark: #2c3d4c;
    --photo-light: #6f8797;
    --white: #ffffff;
  }
  * { box-sizing: border-box; margin: 0; padding: 0; }
  html, body { width: 1200px; height: 873px; overflow: hidden; }
  body {
    background: var(--stage);
    font-family: "Roboto", Arial, sans-serif;
    position: relative;
  }
  .card {
    position: absolute;
    top: 282px;
    width: 540px;
    height: 309px;
    border-radius: 4px;
    box-shadow: 0 6px 18px rgba(0,0,0,0.18);
    overflow: hidden;
  }
  /* contact side */
  .card-contact { left: 40px; background: var(--card-white); }
  .company-name {
    position: absolute; left: 30px; top: 26px;
    font-size: 38px; font-weight: 500; letter-spacing: -0.5px;
    color: var(--blue-mid); text-transform: uppercase;
  }
  .photo-slot {
    position: absolute; right: 22px; top: 62px;
    width: 108px; height: 108px; border-radius: 50%;
    background: var(--white);
    border: 3px solid var(--blue-mid);
    box-shadow: inset 0 4px 8px rgba(0,0,0,0.25);
  }
  .contact-list {
    position: absolute; right: 58px; top: 186px;
    list-style: none; text-align: right;
    font-size: 13px; font-weight: 700; line-height: 19px;
    color: var(--blue-mid); text-transform: uppercase;
  }
  .icon-bar {
    position: absolute; right: 24px; top: 186px;
    width: 26px; height: 78px; border-radius: 4px;
    background: var(--blue-mid);
    display: flex; flex-direction: column; align-items: center; justify-content: space-around;
    padding: 2px 0;
  }
  .icon-bar svg { width: 13px; height: 13px; display: block; }
  .address {
    position: absolute; left: 30px; bottom: 22px;
    font-size: 15px; font-weight: 700; letter-spacing: 0.2px;
    color: var(--blue-mid); text-transform: uppercase;
  }
  /* brand side */
  .card-brand { left: 620px; }
  .brand-photo {
    position: absolute; inset: 0;
    background: linear-gradient(135deg, var(--photo-dark) 0%, #4a6172 45%, var(--photo-light) 100%);
  }
  .brand-name {
    position: absolute; left: 0; right: 0; top: 118px;
    text-align: center;
    font-size: 40px; font-weight: 700; line-height: 44px;
    color: var(--blue-bright); text-transform: uppercase; letter-spacing: 1px;
  }
</style>
</head>
<body>
  <section class="card card-contact">
    <h1 class="company-name">Kestrel Ridge</h1>
    <div class="photo-slot" role="img" aria-label="Space for the loan officer's portrait photo"></div>
    <ul class="contact-list">
      <li>702.519.4827</li>
      <li>702-519-4829</li>
      <li>www.kestrelridgelending,example</li>
      <li>dana@kestrelridgelending.example</li>
    </ul>
    <div class="icon-bar">
      <svg viewBox="0 0 16 16" aria-hidden="true"><path fill="#fff" d="M4 1.5l2.5 3-1.5 1.8c.8 1.8 2 3 3.8 3.8L10.6 8.6l3 2.5-1.2 2.8C7 13.6 2.4 9 2 3z"/></svg>
      <svg viewBox="0 0 16 16" aria-hidden="true"><path fill="#fff" d="M4 1.5l2.5 3-1.5 1.8c.8 1.8 2 3 3.8 3.8L10.6 8.6l3 2.5-1.2 2.8C7 13.6 2.4 9 2 3z"/></svg>
      <svg viewBox="0 0 16 16" aria-hidden="true"><g fill="none" stroke="#fff" stroke-width="1.4"><circle cx="8" cy="8" r="6.3"/><ellipse cx="8" cy="8" rx="2.8" ry="6.3"/><path d="M1.7 8h12.6M2.8 4.8h10.4M2.8 11.2h10.4"/></g></svg>
      <svg viewBox="0 0 16 16" aria-hidden="true"><g fill="none" stroke="#fff" stroke-width="1.4"><rect x="1.5" y="3.5" width="13" height="9"/><path d="M1.5 3.5L8 9l6.5-5.5"/></g></svg>
    </div>
    <p class="address">418 W. Lomita Ave #305 Henderson, NV 89152</p>
  </section>

  <section class="card card-brand">
    <div class="brand-photo" role="img" aria-label="Photo of a person wearing a virtual reality headset in a bright living room, tinted blue-grey"></div>
    <p class="brand-name">Kestrel Ridge<br>Lending</p>
  </section>
</body>
</html>
```